Travel with us to Dunmore's Terrace, Atlantic City

We take groups of people to Atlantic City to gamble. We use a chartered flights which leaves from either Kinston NC or Raleigh NC once a month from each place mentioned above.
First time gamblers pay $249.00 which includes round trip chartered airfare and room for 2 nights based on double occupancy.
Seasoned players from any Dunmores, Pennicks or Tollands properties across the world my have earned enough credit to get their flight and hotel room for free.
I need to see people playing slots and table games as well as boardwalk pictures. I need the dates of my upcoming trips to be shown as well as my contact numbers.
I am taking over my father's business at M and J Travel and I need his name to be used in a very professional way b/c the people know his name NOT the M and J Travel name. His name is Hank Wendell and he recently passed away.
Hotel
- Contact Info for Donna, Marla and Gus
47 Sumner Court
Raleigh NC 27588
Office number: 919.555.0182
Email : qmx58213@fernlinkmail.net
Donna's Cell Number : 305.555.0147
Dates of upcoming trips
Trips leaving Kinston, NC (ISO)
8/1-8/3/2014
9/5-9/7/2014
10/3-10/5/2014
11/7-11/9/2014
12/5-12/7/2014
Trips leaving Raleigh, NC (RDU)
8/8/-8/10/2014
8/17-8/18/2014
9/12-9/14/2014
10/10-10/12/2014
11/14-11/16/2014
12/12-12/14/2014

```html
<!DOCTYPE html>
<html lang="en">
<head>
<meta charset="utf-8">
<title>Dunmore's Terrace Trips – Postcard Back</title>
<link rel="stylesheet" href="https://fonts.googleapis.com/css2?family=Didact+Gothic&family=Mulish:wght@700&display=swap">
<style>
  :root {
    --paper: #ffffff;
    --ink: #262626;
    --tab-green-light: #8cc94a;
    --tab-green-dark: #5c9e2a;
    --kinston-orange: #f7941d;
    --kinston-orange-dark: #ef7f12;
    --raleigh-blue: #33ade3;
    --raleigh-blue-dark: #1e94cf;
    --panel-glass: rgba(255, 255, 255, 0.84);
    --rule: #cfcfcf;
    --stamp-border: #d9d9d9;
  }
  * { box-sizing: border-box; margin: 0; padding: 0; }
  html, body { width: 1200px; height: 930px; overflow: hidden; background: var(--paper); }
  .postcard { position: relative; width: 1200px; height: 930px; background: var(--paper); overflow: hidden; }

  .casino-photo {
    position: absolute; left: 0; top: 0; width: 900px; height: 765px;
    background:
      radial-gradient(ellipse 220px 180px at 640px 110px, rgba(240,120,150,0.85), rgba(240,120,150,0) 70%),
      radial-gradient(ellipse 260px 200px at 760px 40px, rgba(255,190,200,0.7), rgba(255,190,200,0) 70%),
      radial-gradient(ellipse 300px 260px at 420px 620px, rgba(230,90,40,0.75), rgba(230,90,40,0) 70%),
      radial-gradient(ellipse 260px 220px at 200px 300px, rgba(150,120,110,0.8), rgba(150,120,110,0) 70%),
      linear-gradient(90deg, #3a2622 0%, #5a3530 45%, #8a4a4c 70%, #ffffff 97%);
  }

  .address-side { position: absolute; left: 580px; top: 297px; width: 620px; height: 468px; background: var(--paper); }
  .address-line { position: absolute; left: 62px; width: 494px; height: 2px; background: var(--rule); }

  .stamp-box { position: absolute; left: 904px; top: 24px; width: 263px; height: 264px; background: var(--paper); border: 3px solid var(--stamp-border); }

  .schedule-tab {
    position: absolute; left: 0; top: 12px; width: 615px; height: 81px;
    background: linear-gradient(180deg, var(--tab-green-light), var(--tab-green-dark));
    border-radius: 0 24px 24px 0;
    color: var(--paper); font: 700 39px/81px "Mulish", sans-serif; padding-left: 30px;
  }

  .schedule-panel { position: absolute; left: 12px; top: 98px; width: 555px; height: 652px; background: var(--panel-glass); border-radius: 24px; }

  .departure-bar {
    position: absolute; left: 0; width: 552px; height: 55px; padding-left: 18px;
    color: var(--paper); font: 700 31px/55px "Mulish", sans-serif;
  }
  .departure-bar.kinston { top: 2px; background: linear-gradient(180deg, var(--kinston-orange), var(--kinston-orange-dark)); border-radius: 20px 0 0 0; }
  .departure-bar.raleigh { top: 289px; background: linear-gradient(180deg, var(--raleigh-blue), var(--raleigh-blue-dark)); }

  .trip-dates { position: absolute; left: 18px; list-style: none; color: var(--ink); font: 30px/42px "Didact Gothic", sans-serif; }
  .trip-dates.kinston { top: 66px; }
  .trip-dates.raleigh { top: 352px; }
</style>
</head>
<body>
<div class="postcard">
  <div class="casino-photo" role="img" aria-label="Blurred casino floor photo with warm red and pink lights"></div>

  <div class="address-side">
    <div class="address-line" style="top:117px"></div>
    <div class="address-line" style="top:201px"></div>
    <div class="address-line" style="top:283px"></div>
    <div class="address-line" style="top:366px"></div>
  </div>

  <div class="stamp-box" aria-label="Stamp area"></div>

  <div class="schedule-panel">
    <div class="departure-bar kinston">Trips leaving Kinston, NC (ISO)</div>
    <ul class="trip-dates kinston">
      <li>8/1-8/3/2014 (Fri.-Sun.)</li>
      <li>9/5-9/7/2014 (Fri.-Sun.)</li>
      <li>10/3-10/5/2014 (Fri.-Sun.)</li>
      <li>11/7-11/9/2014 (Fri.-Sun.)</li>
      <li>12/5-12/7/2014 (Fri.-Sun.)</li>
    </ul>
    <div class="departure-bar raleigh">Trips leaving Raleigh, NC (RDU)</div>
    <ul class="trip-dates raleigh">
      <li>8/8/-8/10/2014 (Fri.-Sun.)</li>
      <li>8/17-8/18/2014 (Sun.-Mon.)</li>
      <li>9/12-9/14/2014 (Fri.-Sun.)</li>
      <li>10/10-10/12/2014 (Fri.-Sun.)</li>
      <li>10/26-10/27/2014 (Sun.-Mon.)</li>
      <li>11/14-11/16/2014 (Fri.-Sun.)</li>
      <li>12/12-12/14/2014 (Fri.-Sun.)</li>
    </ul>
  </div>

  <div class="schedule-tab">Dates of upcoming trips</div>
</div>
</body>
</html>
```